macro advisory firm intro powerpoint

I have the bones of an introductory deck for a new firm. Need to make it much more professionally designed. Want it to also be customizable when received so I can adjust wording, etc. use colors similar to typical finance firm. high end fonts, etc.

```html
<!DOCTYPE html>
<html lang="en">
<head>
<meta charset="utf-8">
<title>Meridian Crest Macro Advisory – Intro Deck</title>
<link href="https://fonts.googleapis.com/css2?family=Libre+Baskerville:wght@400;700&family=Inter:wght@400;500;700&display=swap" rel="stylesheet">
<style>
:root{
  --bg:#2f3033;
  --navy:#14213a;
  --navy-2:#1d2f4f;
  --beige:#e9dfcb;
  --beige-2:#d9c9a8;
  --paper:#ffffff;
  --ink:#1b1d22;
  --muted:#3a3d44;
  --rule:#e2d7c2;
}
*{margin:0;padding:0;box-sizing:border-box}
html,body{width:983px;height:1200px;overflow:hidden;background:var(--bg)}
body{position:relative;font-family:"Inter",sans-serif;color:var(--ink)}
.slide{position:absolute;width:419px;height:236px;background:var(--paper);overflow:hidden}
.c1{left:60px}.c2{left:505px}
.r1{top:63px}.r2{top:335px}.r3{top:607px}.r4{top:880px}

.head{position:absolute;left:0;top:0;width:100%;height:40px;background:var(--beige)}
.brand{position:absolute;left:9px;top:9px;display:flex;align-items:center;gap:4px}
.brand-dot{width:9px;height:9px;border-radius:50%;background:var(--navy)}
.brand-name{font-family:"Libre Baskerville",serif;font-size:6.6px;line-height:7.4px;color:var(--navy);letter-spacing:.2px}
.head-rule{position:absolute;left:71px;top:4px;width:1px;height:30px;background:var(--navy);opacity:.5}
.head-title{position:absolute;left:83px;top:8px;font-family:"Libre Baskerville",serif;font-size:9.6px;color:var(--navy)}
.head-sub{position:absolute;left:83px;top:24px;font-size:6.2px;color:var(--ink)}

.photo{position:absolute}
.serif{font-family:"Libre Baskerville",serif}
svg.ic{display:block}

/* slide 1 */
.s1-photo{left:0;top:40px;width:100%;height:94px;background:linear-gradient(120deg,#5b5d63,#c6c4bd 45%,#8d8578 75%,#3f3b36)}
.s1-band{position:absolute;left:0;top:165px;width:100%;height:71px;background:var(--navy)}
.s1-card{position:absolute;top:134px;width:129px;height:102px;background:var(--paper);padding:12px 12px 0}
.s1-card h3{font-family:"Libre Baskerville",serif;font-weight:400;font-size:8.4px;color:var(--navy);margin:8px 0 6px}
.s1-card p{font-size:5.1px;line-height:7.7px;color:var(--ink)}

/* slide 2 */
.s2-row{position:absolute;left:0;width:203px;display:flex;gap:10px;padding-left:15px;align-items:center}
.s2-row + .s2-line{}
.s2-line{position:absolute;left:0;width:203px;height:1px;background:#e6e6e6}
.dot-ic{flex:none;width:28px;height:28px;border-radius:50%;background:var(--navy);display:flex;align-items:center;justify-content:center}
.s2-row h3{font-family:"Libre Baskerville",serif;font-weight:400;font-size:7.6px;color:var(--navy);margin-bottom:4px}
.s2-row p{font-size:4.8px;line-height:6.8px;color:var(--ink)}
.s2-photo{left:207px;top:40px;width:212px;height:196px;background:linear-gradient(160deg,#dfe6ec,#aebac4 40%,#6c6a66 70%,#8a6f5c)}

/* slide 3 */
.s3-item{position:absolute;display:flex;align-items:center;gap:8px}
.s3-item h3{font-family:"Libre Baskerville",serif;font-weight:400;font-size:7.4px;color:var(--navy);margin-bottom:3px}
.s3-item p{font-size:4.9px;line-height:6.8px;color:var(--ink)}
.s3-item.left{text-align:right}
.s3-rule{position:absolute;height:1px;width:108px;background:var(--rule)}
.s3-shield{position:absolute;left:137px;top:40px}

/* bio slides */
.bio-shield{position:absolute;left:321px;top:0}
.bio-intro{position:absolute;left:12px;top:53px;border-left:2px solid var(--beige);padding-left:13px;font-size:7.4px;line-height:13px;color:var(--ink);width:300px}
.fact{position:absolute;width:194px;height:54px;border:1px solid var(--navy);display:flex;align-items:center;gap:9px;padding:0 10px}
.fact .bub{flex:none;width:25px;height:25px;border-radius:50%;background:var(--beige);display:flex;align-items:center;justify-content:center}
.fact h4{font-size:7.2px;font-weight:700;color:var(--navy);margin-bottom:4px}
.fact p{font-size:6.1px;line-height:8.6px;color:var(--ink)}
.fa{left:12px}.fb{left:214px}.f1{top:105px}.f2{top:168px}

/* slide 7 */
.svc{position:absolute;top:58px;width:95px;height:157px;background:var(--navy)}
.svc .pic{height:94px}
.svc h3{font-family:"Libre Baskerville",serif;font-weight:400;font-size:7.8px;line-height:9.4px;color:#fff;padding:12px 10px 0}
.svc p{font-size:5.1px;line-height:7.6px;color:#e9e6df;padding:6px 10px 0}

/* slide 8 */
.ben{position:absolute;top:78px;width:96px;text-align:center}
.ben svg.sh{margin:0 auto}
.ben h3{font-family:"Libre Baskerville",serif;font-weight:400;font-size:6.5px;color:var(--navy);margin:9px 0 5px}
.ben p{font-size:5px;line-height:7.6px;color:var(--ink)}
</style>
</head>
<body>

<svg width="0" height="0" style="position:absolute" aria-hidden="true">
  <defs>
    <symbol id="i-doc" viewBox="0 0 24 24"><path d="M6 2h9l4 4v16H6z M15 2v4h4 M9 10h7 M9 13h7 M9 16h7" fill="none" stroke="currentColor" stroke-width="1.4"/></symbol>
    <symbol id="i-case" viewBox="0 0 24 24"><path d="M3 7h18v13H3z M9 7V4h6v3 M3 12h18 M11 11h2v3h-2z" fill="none" stroke="currentColor" stroke-width="1.4"/></symbol>
    <symbol id="i-team" viewBox="0 0 24 24"><g fill="none" stroke="currentColor" stroke-width="1.3"><circle cx="12" cy="12" r="8"/><circle cx="12" cy="10" r="2.2"/><path d="M8 17c1-3 7-3 8 0"/><circle cx="6" cy="9" r="1.6"/><circle cx="18" cy="9" r="1.6"/></g></symbol>
    <symbol id="i-target" viewBox="0 0 24 24"><g fill="none" stroke="currentColor" stroke-width="1.8"><circle cx="12" cy="12" r="8"/><circle cx="12" cy="12" r="4.5"/><path d="M12 12l7-7"/></g></symbol>
    <symbol id="i-hand" viewBox="0 0 24 24"><g fill="none" stroke="currentColor" stroke-width="1.6"><circle cx="12" cy="8" r="3.5"/><path d="M3 16l5-2h5l3 2h5 M3 19h16"/></g></symbol>
    <symbol id="i-user" viewBox="0 0 24 24"><g fill="currentColor"><circle cx="11" cy="8" r="4"/><path d="M4 20c0-5 4-7 7-7 2 0 3 .4 4 1l-1 6z"/><path d="M18 14l1 2 2 .3-1.5 1.4.4 2.2-1.9-1-1.9 1 .4-2.2L15 16.3l2-.3z"/></g></symbol>
    <symbol id="i-bank" viewBox="0 0 24 24"><g fill="none" stroke="currentColor" stroke-width="1.6"><path d="M3 9l9-5 9 5z M5 9v8 M9 9v8 M15 9v8 M19 9v8 M3 19h18"/></g></symbol>
    <symbol id="i-chart" viewBox="0 0 24 24"><g fill="currentColor"><rect x="4" y="14" width="3" height="6"/><rect x="9" y="11" width="3" height="9"/><rect x="14" y="8" width="3" height="12"/><rect x="19" y="5" width="2" height="15"/><path d="M4 11l5-4 4 2 6-5" fill="none" stroke="currentColor" stroke-width="1.4"/></g></symbol>
    <symbol id="i-net" viewBox="0 0 24 24"><g fill="none" stroke="currentColor" stroke-width="1.5"><circle cx="12" cy="12" r="3"/><circle cx="12" cy="3.5" r="1.6"/><circle cx="12" cy="20.5" r="1.6"/><circle cx="3.5" cy="12" r="1.6"/><circle cx="20.5" cy="12" r="1.6"/><path d="M12 5v4 M12 15v4 M5 12h4 M15 12h4"/></g></symbol>
    <symbol id="i-clip" viewBox="0 0 24 24"><g fill="none" stroke="currentColor" stroke-width="1.5"><path d="M6 4h12v17H6z M9 3h6v3H9z M9 10h6 M9 13h6 M9 16h4"/></g></symbol>
    <symbol id="i-shield" viewBox="0 0 24 24"><g fill="none" stroke="currentColor" stroke-width="1.7"><path d="M12 3l8 3v6c0 5-4 8-8 9-4-1-8-4-8-9V6z"/><path d="M8.5 12l2.5 2.5 4.5-5"/></g></symbol>
    <symbol id="i-person" viewBox="0 0 24 24"><g fill="currentColor"><circle cx="12" cy="6.5" r="3.5"/><path d="M5 21c0-6 3-9 7-9s7 3 7 9z"/></g></symbol>
    <symbol id="i-crowd" viewBox="0 0 24 24"><g fill="currentColor"><circle cx="12" cy="8" r="2.5"/><path d="M8 16c0-3 2-5 4-5s4 2 4 5z"/><circle cx="5" cy="14" r="2"/><circle cx="19" cy="14" r="2"/><path d="M2 21c0-2 1.5-4 3-4s3 2 3 4z M16 21c0-2 1.5-4 3-4s3 2 3 4z M12 2v2 M8 3l1 1.5 M16 3l-1 1.5"/></g></symbol>
    <symbol id="i-gear" viewBox="0 0 24 24"><g fill="none" stroke="currentColor" stroke-width="2"><circle cx="12" cy="12" r="3.5"/><path d="M12 3v3 M12 18v3 M3 12h3 M18 12h3 M5.6 5.6l2.1 2.1 M16.3 16.3l2.1 2.1 M5.6 18.4l2.1-2.1 M16.3 7.7l2.1-2.1"/></g></symbol>
    <symbol id="i-arrows" viewBox="0 0 24 24"><g fill="none" stroke="currentColor" stroke-width="2"><path d="M12 13V3 M9 6l3-3 3 3 M12 13L4 7 M4 11V7h4 M12 13l8-6 M16 7h4v4"/><circle cx="12" cy="17" r="3"/></g></symbol>
    <symbol id="i-insight" viewBox="0 0 24 24"><g fill="none" stroke="currentColor" stroke-width="1.8"><circle cx="9" cy="9" r="4.5"/><path d="M12 13l-6 7"/><rect x="15" y="12" width="2.5" height="8" fill="currentColor"/><rect x="19" y="8" width="2.5" height="12" fill="currentColor"/><path d="M9 2v1.5 M4 4l1 1 M14 4l-1 1"/></g></symbol>
  </defs>
</svg>

<!-- 1. Overview -->
<section class="slide c1 r1">
  <header class="head">
    <div class="brand"><span class="brand-dot"></span><span class="brand-name">MERIDIAN<br>CREST</span></div>
    <span class="head-rule"></span>
    <h1 class="head-title">Meridian Crest Macro Advisory, LLP</h1>
    <p class="head-sub">Our goal is to provide strategic and actionable insight today, so our clients are prepared for tomorrow</p>
  </header>
  <div class="photo s1-photo" role="img" aria-label="Photo of advisors reviewing printed financial charts at a table"></div>
  <div class="s1-band"></div>
  <article class="s1-card" style="left:11px">
    <svg class="ic" width="17" height="17" style="color:var(--navy)"><use href="#i-doc"/></svg>
    <h3>Who We Serve</h3>
    <p>C-Suiteexecutives, Financial Institutions ,Hedge Funds, Sovereign Wealth Funds, Family Offices</p>
  </article>
  <article class="s1-card" style="left:147px">
    <svg class="ic" width="20" height="17" style="color:var(--navy)"><use href="#i-case"/></svg>
    <h3>What We Do</h3>
    <p>Decode U.S.Public PolicyTrends Thru a Sophisticated Lens of Economics, Geopolitical Analysis and Deep Relationships</p>
  </article>
  <article class="s1-card" style="left:283px">
    <svg class="ic" width="20" height="19" style="color:var(--navy)"><use href="#i-team"/></svg>
    <h3>Our Team</h3>
    <p>Former Federal and State Government Advisorswho are Economists, Academics and Practitioners</p>
  </article>
</section>

<!-- 2. Introduction -->
<section class="slide c2 r1">
  <header class="head">
    <div class="brand"><span class="brand-dot"></span><span class="brand-name">MERIDIAN<br>CREST</span></div>
    <span class="head-rule"></span>
    <h1 class="head-title">A Strategic Advisory for an Evolving Environment</h1>
    <p class="head-sub">Introduction – Meridian Crest Macro Advisory</p>
  </header>
  <div class="s2-row" style="top:52px">
    <span class="dot-ic"><svg class="ic" width="16" height="16" style="color:#fff"><use href="#i-target"/></svg></span>
    <div><h3>Specialized Focus</h3><p>US policy–Defense and Defense Tech, Government Relation Strategy, Manufacturing, Tax, Trade, International Relation</p></div>
  </div>
  <span class="s2-line" style="top:112px"></span>
  <div class="s2-row" style="top:124px">
    <span class="dot-ic"><svg class="ic" width="16" height="16" style="color:#fff"><use href="#i-hand"/></svg></span>
    <div><h3>Operational Expertise</h3><p>Multi-Billion Dollar Budgets, Public-Private Investment Design, Government Relations Implementation</p></div>
  </div>
  <span class="s2-line" style="top:166px"></span>
  <div class="s2-row" style="top:179px">
    <span class="dot-ic"><svg class="ic" width="15" height="15" style="color:#fff"><use href="#i-user"/></svg></span>
    <div><h3>Client Impact</h3><p>Actionable Guidance for C-suites and institutional investors</p></div>
  </div>
  <div class="photo s2-photo" role="img" aria-label="Photo of a presenter walking colleagues through a chart board in a bright meeting room"></div>
</section>

<!-- 3. Why Clients Seek Us -->
<section class="slide c1 r2">
  <header class="head">
    <div class="brand"><span class="brand-dot"></span><span class="brand-name">MERIDIAN<br>CREST</span></div>
    <span class="head-rule"></span>
    <h1 class="head-title">Why Clients Seek Us</h1>
    <p class="head-sub">Credibility | Access | Results</p>
  </header>
  <div class="s3-item left" style="left:18px;top:73px">
    <div><h3>Institutional Trust</h3><p>Experience at Senior Levels<br>in Private and Public Sector</p></div>
    <span class="dot-ic"><svg class="ic" width="15" height="15" style="color:#fff"><use href="#i-bank"/></svg></span>
  </div>
  <span class="s3-rule" style="left:12px;top:126px"></span>
  <div class="s3-item left" style="left:19px;top:145px">
    <div><h3>Network Advantage</h3><p>Deep Relationships with<br>Policymakers and Regulators</p></div>
    <span class="dot-ic"><svg class="ic" width="16" height="16" style="color:#fff"><use href="#i-net"/></svg></span>
  </div>
  <svg class="s3-shield" width="145" height="184" viewBox="0 0 145 184" role="img" aria-label="Photo of a domed government capitol building against a blue sky">
    <defs><linearGradient id="sky" x1="0" y1="0" x2="0" y2="1"><stop offset="0" stop-color="#2f5fa8"/><stop offset=".55" stop-color="#7fa2d6"/><stop offset="1" stop-color="#d8d2c4"/></linearGradient></defs>
    <path d="M0 0H145V112Q145 160 72.5 184Q0 160 0 112Z" fill="var(--beige-2)"/>
    <path d="M4 0H141V110Q141 155 72.5 178Q4 155 4 110Z" fill="url(#sky)"/>
  </svg>
  <div class="s3-item" style="left:292px;top:73px">
    <span class="dot-ic"><svg class="ic" width="15" height="15" style="color:#fff"><use href="#i-chart"/></svg></span>
    <div><h3>Analytic Rigor</h3><p>Advanced Modeling &amp; Proprietary<br>Scenario Frameworks</p></div>
  </div>
  <span class="s3-rule" style="left:298px;top:126px"></span>
  <div class="s3-item" style="left:285px;top:148px">
    <span class="dot-ic"><svg class="ic" width="15" height="15" style="color:#fff"><use href="#i-clip"/></svg></span>
    <div><h3>Outcome Focused</h3><p>Insight built to drive decisions—not<br>just commentary</p></div>
  </div>
</section>

<!-- 4. Co-founder -->
<section class="slide c2 r2">
  <header class="head">
    <div class="brand"><span class="brand-dot"></span><span class="brand-name">MERIDIAN<br>CREST</span></div>
    <span class="head-rule"></span>
    <h1 class="head-title">Adrian Castell-Hayes, Ph.D, MBA</h1>
    <p class="head-sub">Co-Founder</p>
  </header>
  <svg class="bio-shield" width="83" height="97" viewBox="0 0 83 97" role="img" aria-label="Portrait of Adrian Castell-Hayes">
    <defs><linearGradient id="p1" x1="0" y1="0" x2="0" y2="1"><stop offset="0" stop-color="#5a4a3e"/><stop offset="1" stop-color="#141820"/></linearGradient></defs>
    <path d="M0 0H83V52Q83 80 41.5 97Q0 80 0 52Z" fill="url(#p1)"/>
  </svg>
  <p class="bio-intro">Economic Strategist | Author | Captain U.S. Army Reserve<br>(SME Finance &amp; Banking) | Deputy Chief of Staff, Governor Alan Brooks</p>
  <div class="fact fa f1"><span class="bub"><svg width="14" height="14" style="color:var(--navy)"><use href="#i-bank"/></svg></span><div><h4>Government &amp; Budget Leadership</h4><p>$87B+ oversight, economic competitiveness strategy for Virginia</p></div></div>
  <div class="fact fb f1"><span class="bub"><svg width="14" height="14" style="color:var(--navy)"><use href="#i-shield"/></svg></span><div><h4>Defense Sector Expertise</h4><p>Captain, U.S. Army Reserve – Civil Affairs, Financial Specialization</p></div></div>
  <div class="fact fa f2"><span class="bub"><svg width="14" height="14" style="color:var(--navy)"><use href="#i-person"/></svg></span><div><h4>Cross-Sector Executive</h4><p>Northfield Holdings (Investments), Keystone Policy Advisors (Consulting)</p></div></div>
  <div class="fact fb f2"><span class="bub"><svg width="14" height="14" style="color:var(--navy)"><use href="#i-crowd"/></svg></span><div><h4>Thought Leadership</h4><p>Author, policy lecturer, media contributor (Market Desk, Capital Journal, Civic Radio)</p></div></div>
</section>

<!-- 5. Co-founder -->
<section class="slide c1 r3">
  <header class="head">
    <div class="brand"><span class="brand-dot"></span><span class="brand-name">MERIDIAN<br>CREST</span></div>
    <span class="head-rule"></span>
    <h1 class="head-title">Thomas R. Avery, MBA</h1>
    <p class="head-sub">Co-Founder</p>
  </header>
  <svg class="bio-shield" width="83" height="97" viewBox="0 0 83 97" role="img" aria-label="Portrait of Thomas R. Avery">
    <defs><linearGradient id="p2" x1="0" y1="0" x2="0" y2="1"><stop offset="0" stop-color="#6f8a4a"/><stop offset=".5" stop-color="#8f7b6a"/><stop offset="1" stop-color="#1a1f2a"/></linearGradient></defs>
    <path d="M0 0H83V52Q83 80 41.5 97Q0 80 0 52Z" fill="url(#p2)"/>
  </svg>
  <p class="bio-intro">Virginia Dept. Sec. Commerce &amp; Trade | Global Financial Services Executive |<br>Major US Army Reserve –SME Banking &amp; Finance</p>
  <div class="fact fa f1"><span class="bub"><svg width="14" height="14" style="color:var(--navy)"><use href="#i-bank"/></svg></span><div><h4>Public Sector Leadership</h4><p>Deputy Secretary of Commerce &amp; Trade, Commonwealth of Virginia</p></div></div>
  <div class="fact fb f1"><span class="bub"><svg width="14" height="14" style="color:var(--navy)"><use href="#i-shield"/></svg></span><div><h4>Private Sector Finance</h4><p>Senior roles at Halvorsen Bank and other major financial institutions</p></div></div>
  <div class="fact fa f2"><span class="bub"><svg width="14" height="14" style="color:var(--navy)"><use href="#i-person"/></svg></span><div><h4>Capital Markets Expertise</h4><p>Decades of experience in banking, trade, and investment strategy</p></div></div>
  <div class="fact fb f2"><span class="bub"><svg width="14" height="14" style="color:var(--navy)"><use href="#i-crowd"/></svg></span><div><h4>Defense Experience</h4><p>Major, U.S. Army Reserve – Civil Affairs, Finance &amp; Banking</p></div></div>
</section>

<!-- 6. Co-founder -->
<section class="slide c2 r3">
  <header class="head">
    <div class="brand"><span class="brand-dot"></span><span class="brand-name">MERIDIAN<br>CREST</span></div>
    <span class="head-rule"></span>
    <h1 class="head-title">Robert Langford, MBA, MPA</h1>
    <p class="head-sub">Co-Founder</p>
  </header>
  <svg class="bio-shield" width="83" height="97" viewBox="0 0 83 97" role="img" aria-label="Portrait of Robert Langford">
    <defs><linearGradient id="p3" x1="0" y1="0" x2="0" y2="1"><stop offset="0" stop-color="#ffffff"/><stop offset=".35" stop-color="#8a5a3c"/><stop offset="1" stop-color="#1c2230"/></linearGradient></defs>
    <path d="M0 0H83V52Q83 80 41.5 97Q0 80 0 52Z" fill="url(#p3)"/>
  </svg>
  <p class="bio-intro">Founder, The Langford Group | Policy &amp; Financial Services Strategy Executive|<br>Lt.CommanderUS Navy Reserve (RET)</p>
  <div class="fact fa f1"><span class="bub"><svg width="14" height="14" style="color:var(--navy)"><use href="#i-bank"/></svg></span><div><h4>Policy Advisory</h4><p>Former Special Assistant to the President; legislative strategist</p></div></div>
  <div class="fact fb f1"><span class="bub"><svg width="14" height="14" style="color:var(--navy)"><use href="#i-shield"/></svg></span><div><h4>Finance &amp; Advocacy</h4><p>Managing Director, Alpine Trust; SVP, Fixed Income Assoc./FIMA</p></div></div>
  <div class="fact fa f2"><span class="bub"><svg width="14" height="14" style="color:var(--navy)"><use href="#i-person"/></svg></span><div><h4>Strategic Communications</h4><p>Founder of The Langford Group; 20+ years in public/private engagement</p></div></div>
  <div class="fact fb f2"><span class="bub"><svg width="14" height="14" style="color:var(--navy)"><use href="#i-crowd"/></svg></span><div><h4>Network Capital</h4><p>Bridges policy, finance, and stakeholder relations at national scale</p></div></div>
</section>

<!-- 7. Advisory Services -->
<section class="slide c1 r4">
  <header class="head">
    <div class="brand"><span class="brand-dot"></span><span class="brand-name">MERIDIAN<br>CREST</span></div>
    <span class="head-rule"></span>
    <h1 class="head-title">Advisory Services</h1>
    <p class="head-sub">Flexible Models for Strategic Insight &amp; Engagement</p>
  </header>
  <article class="svc" style="left:12px">
    <div class="pic" role="img" aria-label="Photo of an advisor signing a financial report" style="background:linear-gradient(160deg,#8a7a66,#2a3a5e 55%,#c9d3e0)"></div>
    <h3>Retainer Advisory</h3>
    <p>Access to Senior Advisors, Regular Updates, Strategic counsel</p>
  </article>
  <article class="svc" style="left:113px">
    <div class="pic" role="img" aria-label="Photo of two consultants working together at a laptop" style="background:linear-gradient(160deg,#6b5a4a,#c9bcae 50%,#8a6c52)"></div>
    <h3>Project-Based<br>Engagements</h3>
    <p>In-depth, Bespoke Studies with Actionable Recommendations</p>
  </article>
  <article class="svc" style="left:215px">
    <div class="pic" role="img" aria-label="Photo of a hand over glowing market bar charts" style="background:linear-gradient(160deg,#2b4d6a,#8fb4cc 50%,#3b4f66)"></div>
    <h3>Market Entry &amp;<br>Due Diligence</h3>
    <p>Full-Spectrum Support for Cross-Border and Regulatory Risk, Strategic Introductions</p>
  </article>
  <article class="svc" style="left:315px">
    <div class="pic" role="img" aria-label="Overhead photo of a speaker addressing a boardroom table" style="background:linear-gradient(160deg,#f0f0f0,#c8c6c2 50%,#6b6258)"></div>
    <h3>Speakers</h3>
    <p>Speakers for Board Meetings, Client Conferences, Curate Panels</p>
  </article>
</section>

<!-- 8. Client Benefits -->
<section class="slide c2 r4">
  <header class="head">
    <div class="brand"><span class="brand-dot"></span><span class="brand-name">MERIDIAN<br>CREST</span></div>
    <span class="head-rule"></span>
    <h1 class="head-title">Client Benefits</h1>
    <p class="head-sub">Turning Complexity Into Competitive Advantage</p>
  </header>
  <div class="ben" style="left:16px">
    <svg class="sh" width="51" height="70" viewBox="0 0 51 70"><path d="M0 0H51V42Q51 58 25.5 70Q0 58 0 42Z" fill="var(--navy)"/><use href="#i-gear" x="13" y="17" width="25" height="25" style="color:#fff"/></svg>
    <h3>Risk Mitigation</h3><p>Timely policy insight reduces exposure and regulatory surprises</p>
  </div>
  <div class="ben" style="left:110px">
    <svg class="sh" width="51" height="70" viewBox="0 0 51 70"><path d="M0 0H51V42Q51 58 25.5 70Q0 58 0 42Z" fill="var(--navy)"/><use href="#i-arrows" x="13" y="16" width="25" height="25" style="color:#fff"/></svg>
    <h3>Improved Decisions</h3><p>Data-informed strategies accelerate institutional action</p>
  </div>
  <div class="ben" style="left:206px">
    <svg class="sh" width="51" height="70" viewBox="0 0 51 70"><path d="M0 0H51V42Q51 58 25.5 70Q0 58 0 42Z" fill="var(--navy)"/><use href="#i-net" x="13" y="16" width="25" height="25" style="color:#fff"/></svg>
    <h3>Access to Networks</h3><p>Connect with U.S. stakeholders and decision-makers</p>
  </div>
  <div class="ben" style="left:305px">
    <svg class="sh" width="51" height="70" viewBox="0 0 51 70"><path d="M0 0H51V42Q51 58 25.5 70Q0 58 0 42Z" fill="var(--navy)"/><use href="#i-insight" x="13" y="16" width="25" height="25" style="color:#fff"/></svg>
    <h3>Custom Insight</h3><p>Tailored economic and geopolitical analysis—not generic commentary</p>
  </div>
</section>

</body>
</html>
```